217 Marlow Lane Residences

designing a sign for apartment complex;
prefer colors gray white and yellow

Target Market(s)

residents coming home to their apartment

Font styles to use
Serif
Sans Serif

Colors
FFF300
FFF600
FEFA6F
FFFEC7
FFFEE8

Requirements
Must have
• black or gray, white and some yellow; easy to read and see

```html
<!DOCTYPE html>
<html lang="en">
<head>
<meta charset="utf-8">
<title>217 Marlow Lane Residences – Sign Options</title>
<link rel="stylesheet" href="https://fonts.googleapis.com/css2?family=Poppins:wght@400;500;600;700;800&display=swap">
<style>
  :root {
    --yellow: #e6e500;
    --charcoal: #2a2a2a;
    --grey-frame: #c3c3c3;
    --grey-banner: #c4c4c4;
    --white: #ffffff;
    --label: #333333;
  }
  * { margin: 0; padding: 0; box-sizing: border-box; }
  html, body { width: 1200px; height: 2640px; overflow: hidden; background: var(--white); }
  body { position: relative; font-family: 'Poppins', sans-serif; }

  .option-label { position: absolute; left: 134px; font-size: 28px; font-weight: 400; color: var(--label); letter-spacing: -0.5px; }

  .sign { position: absolute; left: 134px; width: 930px; box-shadow: 22px 28px 40px rgba(0,0,0,0.28); overflow: hidden; }
  .sign-face { position: absolute; left: 20px; right: 20px; top: 22px; }

  .sign--yellow { top: 178px; height: 658px; background: var(--grey-frame); }
  .sign--yellow .sign-face { height: 490px; background: var(--yellow); }
  .sign--dark-band { top: 1030px; height: 659px; background: var(--yellow); }
  .sign--dark-band .sign-face { height: 490px; background: var(--charcoal); }
  .sign--dark-full { top: 1862px; height: 659px; background: var(--yellow); }
  .sign--dark-full .sign-face { bottom: 22px; background: var(--charcoal); }

  .brand-name { position: absolute; top: 52px; left: 0; right: 0; text-align: center; font-size: 78px; font-weight: 500; letter-spacing: 14px; color: var(--charcoal); line-height: 1; }

  .address { position: absolute; left: 0; right: 0; text-align: center; font-weight: 800; line-height: 0.9; letter-spacing: -1px; }
  .address span { display: block; }
  .sign--yellow .address { top: 170px; font-size: 112px; color: #1d1d1d; }
  .sign--dark-band .address { top: 28px; font-size: 122px; line-height: 0.87; color: var(--white); }
  .sign--dark-full .address { top: 40px; font-size: 126px; line-height: 0.82; color: var(--white); }
  .sign--dark-full .address .house-number { font-size: 200px; color: var(--yellow); margin-bottom: 6px; }

  .residences-banner { position: absolute; }
  .residences-banner svg { position: absolute; inset: 0; width: 100%; height: 100%; }
  .residences-banner .banner-text { position: absolute; top: 0; bottom: 0; display: flex; align-items: center; justify-content: center; font-weight: 700; letter-spacing: -1px; }
  .sign--yellow .residences-banner { left: 116px; top: 366px; width: 690px; height: 105px; }
  .sign--yellow .banner-text { left: 50px; width: 450px; font-size: 72px; color: var(--white); }
  .sign--dark-band .residences-banner { left: 116px; top: 366px; width: 690px; height: 105px; }
  .sign--dark-band .banner-text { left: 50px; width: 450px; font-size: 72px; color: var(--charcoal); }
  .sign--dark-full .residences-banner { left: 45px; top: 457px; width: 798px; height: 121px; }
  .sign--dark-full .banner-text { left: 60px; width: 520px; font-size: 82px; color: var(--charcoal); }

  .contact-band { position: absolute; left: 0; right: 0; bottom: 0; height: 146px; }
  .sign--yellow .contact-band { background: var(--charcoal); color: var(--white); }
  .sign--dark-band .contact-band { background: linear-gradient(100deg, #ffffff 45%, #f2f2f2 70%, #d6d6d6 100%); color: #111; }
  .call-line { position: absolute; top: 10px; left: 0; right: 0; text-align: center; font-size: 74px; font-weight: 600; letter-spacing: -2px; line-height: 1.1; white-space: nowrap; }
  .sign--yellow .call-label { color: var(--yellow); }
  .call-label { margin-right: 28px; }
  .web-line { position: absolute; top: 94px; left: 20px; right: 20px; display: flex; align-items: center; justify-content: center; gap: 18px; font-size: 28px; font-weight: 600; white-space: nowrap; }
  .web-line .icon { width: 28px; height: 28px; flex: none; }
  .web-line .email-icon { margin-left: 12px; }
  .sign--yellow .icon { stroke: var(--yellow); }
  .sign--dark-band .icon { stroke: #222; }
</style>
</head>
<body>

<p class="option-label" style="top:114px">SAMPLE 1</p>
<section class="sign sign--yellow">
  <div class="sign-face">
    <div class="brand-name">HALVERN</div>
    <h1 class="address"><span>217 MARLOW</span><span>LANE</span></h1>
    <div class="residences-banner">
      <svg viewBox="0 0 690 105" preserveAspectRatio="none" aria-hidden="true">
        <polygon points="0,0 500,0 548,52.5 500,105 0,105 48,52.5" fill="var(--charcoal)"/>
        <polygon points="540,0 582,0 630,52.5 582,105 540,105 588,52.5" fill="var(--charcoal)"/>
        <polygon points="600,0 642,0 690,52.5 642,105 600,105 648,52.5" fill="var(--charcoal)"/>
      </svg>
      <div class="banner-text">RESIDENCES</div>
    </div>
  </div>
  <div class="contact-band">
    <div class="call-line"><span class="call-label">CALL US :</span><span class="call-number">01632 960 418</span></div>
    <div class="web-line">
      <svg class="icon" viewBox="0 0 28 28" fill="none" stroke-width="1.6"><circle cx="14" cy="14" r="12"/><ellipse cx="14" cy="14" rx="5.5" ry="12"/><line x1="2" y1="14" x2="26" y2="14"/><line x1="4" y1="8" x2="24" y2="8"/><line x1="4" y1="20" x2="24" y2="20"/></svg>
      <span>www.marlowliving.com</span>
      <svg class="icon email-icon" viewBox="0 0 28 28" fill="none" stroke-width="1.8"><rect x="2" y="6" width="24" height="16"/><polyline points="2,6 14,16 26,6"/><line x1="2" y1="22" x2="11" y2="13.5"/><line x1="26" y1="22" x2="17" y2="13.5"/></svg>
      <span>hello@marlowliving.com</span>
    </div>
  </div>
</section>

<p class="option-label" style="top:976px">SAMPLE 2</p>
<section class="sign sign--dark-band">
  <div class="sign-face">
    <h1 class="address"><span>217</span><span>MARLOW</span><span>LANE</span></h1>
    <div class="residences-banner">
      <svg viewBox="0 0 690 105" preserveAspectRatio="none" aria-hidden="true">
        <polygon points="0,0 500,0 548,52.5 500,105 0,105 48,52.5" fill="var(--grey-banner)"/>
        <polygon points="540,0 582,0 630,52.5 582,105 540,105 588,52.5" fill="var(--grey-banner)"/>
        <polygon points="600,0 642,0 690,52.5 642,105 600,105 648,52.5" fill="var(--grey-banner)"/>
      </svg>
      <div class="banner-text">RESIDENCES</div>
    </div>
  </div>
  <div class="contact-band">
    <div class="call-line"><span class="call-label">CALL US :</span><span class="call-number">01632 960 418</span></div>
    <div class="web-line">
      <svg class="icon" viewBox="0 0 28 28" fill="none" stroke-width="1.6"><circle cx="14" cy="14" r="12"/><ellipse cx="14" cy="14" rx="5.5" ry="12"/><line x1="2" y1="14" x2="26" y2="14"/><line x1="4" y1="8" x2="24" y2="8"/><line x1="4" y1="20" x2="24" y2="20"/></svg>
      <span>www.marlowliving.com</span>
      <svg class="icon email-icon" viewBox="0 0 28 28" fill="none" stroke-width="1.8"><rect x="2" y="6" width="24" height="16"/><polyline points="2,6 14,16 26,6"/><line x1="2" y1="22" x2="11" y2="13.5"/><line x1="26" y1="22" x2="17" y2="13.5"/></svg>
      <span>hello@marlowliving.com</span>
    </div>
  </div>
</section>

<p class="option-label" style="top:1802px">SAMPLE 3</p>
<section class="sign sign--dark-full">
  <div class="sign-face">
    <h1 class="address"><span class="house-number">217</span><span>MARLOW</span><span>LANE</span></h1>
    <div class="residences-banner">
      <svg viewBox="0 0 798 121" preserveAspectRatio="none" aria-hidden="true">
        <defs>
          <linearGradient id="metal" x1="0" y1="0" x2="1" y2="0">
            <stop offset="0" stop-color="#8f8f8f"/>
            <stop offset="0.25" stop-color="#e4e4e4"/>
            <stop offset="0.5" stop-color="#a3a3a3"/>
            <stop offset="0.8" stop-color="#f4f4f4"/>
            <stop offset="1" stop-color="#ffffff"/>
          </linearGradient>
        </defs>
        <polygon points="0,0 590,0 646,60.5 590,121 0,121 56,60.5" fill="url(#metal)"/>
        <polygon points="628,0 672,0 728,60.5 672,121 628,121 684,60.5" fill="url(#metal)"/>
        <polygon points="698,0 742,0 798,60.5 742,121 698,121 754,60.5" fill="#ffffff"/>
      </svg>
      <div class="banner-text">RESIDENCES</div>
    </div>
  </div>
</section>

</body>
</html>
```